Plakat-Design für Musikwettbewerb-Veranstalter
Zielgruppe
Wir veranstalten Musikwettbewerbe an Schulen. Zielgruppe sind Schüler und ihre Eltern, männlich/weiblich 40/60, u25/ü25 ca. 50/50
Aufgabenstellung
Wir sind gespannt, gerne frei denken, Logo anbei, weitere Infos auf der Homepage www.klangfuchs-wettbewerb.de, Inhalte lt. altem Plakat (ebenfalls anbei)

```html
<!DOCTYPE html>
<html lang="de">
<head>
<meta charset="utf-8">
<title>Klangfuchs – Vorentscheid Nordhagen</title>
<link rel="stylesheet" href="https://fonts.googleapis.com/css2?family=Archivo+Black&family=Alfa+Slab+One&family=Audiowide&family=Josefin+Sans:wght@700&family=Oswald:wght@300&display=swap">
<style>
  :root {
    --pink: #e6007e;
    --blue: #2aa9e0;
    --green: #95c11f;
    --purple: #612482;
    --orange: #f39200;
    --yellow: #f6e500;
    --white: #ffffff;
    --ink: #1d1d1b;
    --footer: #6f6a72;
  }
  html, body {
    margin: 0;
    padding: 0;
    width: 846px;
    height: 1200px;
    overflow: hidden;
    background: #ffffff;
  }
  .poster {
    display: block;
    width: 846px;
    height: 1200px;
  }
  .title {
    font-family: "Archivo Black", "Arial Black", sans-serif;
    fill: var(--white);
    font-size: 104px;
    letter-spacing: -5px;
  }
  .slab {
    font-family: "Alfa Slab One", Georgia, serif;
    fill: var(--white);
  }
  .school {
    font-family: "Audiowide", "Arial", sans-serif;
    font-style: italic;
    font-size: 22px;
    fill: none;
    stroke: var(--white);
    stroke-width: 1.3px;
    letter-spacing: 1px;
  }
  .info-strong {
    font-family: "Josefin Sans", "Arial", sans-serif;
    font-weight: 700;
    font-size: 16px;
    letter-spacing: 2px;
    fill: var(--ink);
  }
  .info-light {
    font-family: "Oswald", "Arial Narrow", sans-serif;
    font-weight: 300;
    font-size: 14px;
    letter-spacing: 2.5px;
    fill: var(--ink);
  }
  .web {
    font-family: "Oswald", "Arial Narrow", sans-serif;
    font-weight: 300;
    font-size: 26px;
    letter-spacing: 4px;
    fill: var(--white);
  }
</style>
</head>
<body>
<svg class="poster" viewBox="0 0 846 1200" xmlns="http://www.w3.org/2000/svg">
  <defs>
    <linearGradient id="stage-bg" x1="0" y1="0" x2="0.4" y2="1">
      <stop offset="0" stop-color="#cdb8c6"/>
      <stop offset="0.45" stop-color="#f2bcd6"/>
      <stop offset="0.8" stop-color="#f3d4ef"/>
      <stop offset="1" stop-color="#cdb5de"/>
    </linearGradient>
    <radialGradient id="glow" cx="0.5" cy="0.5" r="0.5">
      <stop offset="0" stop-color="#fffbe6" stop-opacity="0.95"/>
      <stop offset="1" stop-color="#fffbe6" stop-opacity="0"/>
    </radialGradient>
    <linearGradient id="instruments-tones" x1="0" y1="0" x2="1" y2="0.3">
      <stop offset="0" stop-color="#e6007e"/>
      <stop offset="0.3" stop-color="#f39200"/>
      <stop offset="0.5" stop-color="#612482"/>
      <stop offset="0.7" stop-color="#95c11f"/>
      <stop offset="1" stop-color="#f6e500"/>
    </linearGradient>
    <linearGradient id="footer-bg" x1="0" y1="0" x2="1" y2="0">
      <stop offset="0" stop-color="#77636f"/>
      <stop offset="0.5" stop-color="#747276"/>
      <stop offset="1" stop-color="#5c5268"/>
    </linearGradient>
  </defs>

  <!-- stage background -->
  <rect class="stage" width="846" height="1084" fill="url(#stage-bg)"/>
  <ellipse cx="300" cy="620" rx="150" ry="70" fill="url(#glow)"/>
  <ellipse cx="680" cy="490" rx="80" ry="60" fill="url(#glow)"/>
  <ellipse cx="440" cy="1030" rx="160" ry="60" fill="url(#glow)"/>

  <!-- instruments illustration area -->
  <rect class="instruments" x="60" y="30" width="720" height="400" rx="160" ry="140"
        fill="url(#instruments-tones)" opacity="0.75"
        role="img" aria-label="Farbige Silhouetten von Musikinstrumenten: Gitarren, Tuba, Mikrofon, Schlagzeug, Flügel und Keyboard mit Farbspritzern"/>

  <!-- event name -->
  <text class="title" x="423" y="300" text-anchor="middle">Klangfuchs</text>

  <!-- vorentscheid badge -->
  <ellipse cx="375" cy="492" rx="247" ry="91" fill="var(--purple)"/>
  <polygon points="121,401 594,459 550,532 170,550" fill="var(--blue)"/>
  <text class="slab" x="212" y="450" font-size="33" letter-spacing="6" transform="rotate(6.5 212 450)">VORENTSCHEID</text>
  <text class="slab" x="241" y="534" font-size="26" letter-spacing="4" transform="rotate(-3 241 534)">NORDHAGEN</text>

  <!-- date badge -->
  <ellipse cx="627" cy="590" rx="128" ry="64" fill="var(--orange)"/>
  <polygon points="485,572 701,516 749,624 492,631" fill="var(--green)"/>
  <text class="slab" x="623" y="586" font-size="27" letter-spacing="2" text-anchor="middle" transform="rotate(-7 623 586)">11.07.16</text>
  <text class="slab" x="621" y="618" font-size="20" letter-spacing="2" text-anchor="middle" transform="rotate(-7 621 618)">AB 19:00 UHR</text>

  <!-- participating schools -->
  <polygon class="band band-pink" points="0,688 443,589 515,668 0,739" fill="var(--pink)"/>
  <text class="school" x="14" y="712" transform="rotate(-12 14 712)">LINDENHOF-SCHULE</text>

  <polygon class="band band-blue" points="0,748 488,698 554,791 0,797" fill="var(--blue)"/>
  <text class="school" x="16" y="780" transform="rotate(-5 16 780)">BERUFLICHE SCHULE NORDHAGEN</text>

  <polygon class="band band-green" points="0,813 593,822 652,917 0,863" fill="var(--green)"/>
  <text class="school" x="14" y="844" transform="rotate(4 14 844)">GEMEINSCHAFTSSCHULE NORDHAGEN</text>

  <!-- venue -->
  <text class="info-strong" x="283" y="960" text-anchor="middle">MENSA DER</text>
  <text class="info-strong" x="283" y="987" text-anchor="middle">LINDENHOF-SCHULE</text>
  <text class="info-light" x="283" y="1013" text-anchor="middle">LINDENHOFWEG 12</text>
  <text class="info-light" x="283" y="1034" text-anchor="middle">25870 NORDHAGEN</text>

  <!-- times and tickets -->
  <text class="info-strong" x="512" y="962">EINLASS: 18:30 UHR</text>
  <text class="info-strong" x="512" y="989">BEGINN: 19:00 UHR</text>
  <text class="info-light" x="513" y="1013">VORVERKAUF: 3€</text>
  <text class="info-light" x="513" y="1034">ABENDKASSE: 4€</text>

  <!-- footer -->
  <rect class="footer" y="1084" width="846" height="116" fill="url(#footer-bg)"/>
  <circle cx="130" cy="1142" r="5" fill="var(--white)"/>
  <text class="web" x="423" y="1152" text-anchor="middle">WWW.KLANGFUCHS-WETTBEWERB.DE</text>
  <circle cx="716" cy="1142" r="5" fill="var(--white)"/>
</svg>
</body>
</html>
```